Brightgate Automotive Service Website Design

We are working with Brightgate Automotive Service. They are a local mechanic/garage and in need of a new website design.

Some sites to use for inspiration:

https://www.torvalle.example
https://www.quenby.example
https://parks-carcare.example
https://www.hollowmerefullautocare.example/

Thank you for taking the time to consider designing a website for us. We are web developers based in Stockton, CA, USA. Most of our projects go through the same process. Understanding this process may help you win a project with us. We custom-code all of our websites in-house. We don’t have any requirements as to what tools you use for your design, but we prefer Figma files. For any design that we label as four-stars, we send it to the client for review. The client picks the final design they want us to use. Once we complete this process, we will continue to show additional clients all the four-star sites and purchase them later. Your designs will have multiple chances to sell. For better chances of success, we ask that you follow these guidelines.

IMAGES:
If you use any images or icons in the design, we ask that you have a link to the asset so we can purchase the image/icon. Most of the designs we submit do not have the customer’s images on them unless they have some great images. Be creative; show us the feeling you are trying to portray with your image choices. Use any royalty-free site you choose. We subscribe to Adobe and mainly use their images, but we can purchase images outside of Adobe.

PLEASE NOTE: we will not submit designs to clients with watermarks on the images.

FONTS:
We ask that you identify the fonts used in the design. This can be done in a message if you want. We typically use Google Fonts and Adobe Fonts.

CONTENT:
We're always open to different content and ideas. We often submit designs with stock images so the client can see our vision. We typically take pictures after the website launch to use their images with our vision. Lorem Ipsum is fine for paragraphs, but we ask that you write the headers in correct English. We want to be able to show the vision and identify the sections of the website.

INSPIRATION:
We typically add a couple of links in the brief of websites we like to help you get started in your design.

REVISIONS:
We do not often ask for revisions of the designs unless we see something in the design that may not appeal to the client. If there are slight changes that we want to make, we do that in the development process.

FEEDBACK:
We rarely give feedback on designs during the design process. We are working on many website projects and do not have the time to provide feedback. We usually respond if your request is well thought out and asks specific questions, but a note asking “feedback, please” usually goes unanswered.

```html
<!DOCTYPE html>
<html lang="en">
<head>
<meta charset="utf-8">
<title>Brightgate Automotive Service</title>
<link href="https://fonts.googleapis.com/css2?family=Oswald:wght@400;500;600;700&family=Roboto:wght@400;500;700&display=swap" rel="stylesheet">
<style>
:root{
  --red:#b50d0d;
  --red-bright:#d0141a;
  --black:#000;
  --ink:#111;
  --grey-head:#8a8a8a;
  --grey-text:#777;
  --light:#f2f2f2;
  --white:#fff;
}
*{margin:0;padding:0;box-sizing:border-box}
html,body{width:1200px;height:3616px;overflow:hidden}
body{position:relative;font-family:"Roboto",Arial,sans-serif;background:var(--white);color:var(--ink)}
.abs{position:absolute}
.head{font-family:"Oswald","Arial Narrow",sans-serif;font-weight:700;text-transform:uppercase}

/* header */
.site-header{left:0;top:0;width:1200px;height:80px;background:var(--black)}
.brand{left:143px;top:18px;font-family:"Oswald",sans-serif;font-weight:700;font-size:34px;line-height:44px;color:#9a9a9a;letter-spacing:-1px;text-transform:uppercase}
.nav a{position:absolute;top:0;height:80px;line-height:80px;color:var(--white);font-family:"Oswald",sans-serif;font-weight:500;font-size:14px;text-decoration:none;letter-spacing:.3px}
.nav .active{background:var(--red);width:59px;text-align:center}
.book-btn{left:939px;top:22px;width:116px;height:36px;background:var(--red);color:var(--white);font-family:"Oswald",sans-serif;font-weight:600;font-size:14px;line-height:36px;text-align:center}

/* hero */
.hero{left:0;top:80px;width:1200px;height:560px;background:linear-gradient(90deg,#1c1c1c 0%,#3a3a3a 45%,#2a2a2a 100%)}
.hero-panel{left:600px;top:80px;width:455px;height:560px;background:linear-gradient(160deg,#cfc3ad 0%,#b7433c 55%,#7a1414 100%)}
.hero-title{left:142px;top:205px;font-size:48px;line-height:48px;color:var(--white)}
.hero-title span{color:var(--red-bright)}
.btn-red{background:var(--red);color:var(--white);font-family:"Oswald",sans-serif;font-weight:600;font-size:14px;text-align:center}
.hero-arrow{width:30px;height:30px;background:#7a7a7a;color:var(--white);text-align:center;line-height:28px;font-size:18px}

/* service strip */
.svc{top:640px;height:267px;overflow:hidden}
.svc h3{position:absolute;left:76px;top:30px;font-family:"Oswald",sans-serif;font-weight:500;font-size:26px;line-height:32px;color:var(--white)}
.svc p{position:absolute;left:76px;top:106px;width:220px;font-size:12.5px;line-height:24px;color:var(--white)}
.svc .outline-btn{position:absolute;left:76px;top:189px;width:109px;height:36px;border:2px solid var(--white);color:var(--white);font-family:"Oswald",sans-serif;font-weight:600;font-size:13px;line-height:32px;text-align:center}
.svc .num{position:absolute;left:205px;top:150px;font-family:"Oswald",sans-serif;font-weight:700;font-size:118px;line-height:130px;color:rgba(255,255,255,.18)}

/* section titles */
.sec-title{width:1200px;left:0;text-align:center;font-size:42px;color:var(--grey-head)}
.sec-title span{color:var(--red)}

/* offer */
.offer{width:275px;text-align:center}
.offer .ico{width:78px;height:78px;border-radius:50%;background:#fbe4e4;margin:0 auto;display:flex;align-items:center;justify-content:center}
.offer.active .ico{background:var(--red)}
.offer h4{font-family:"Oswald",sans-serif;font-weight:500;font-size:20px;margin-top:14px;color:var(--ink)}
.offer p{font-size:12.5px;line-height:24px;color:var(--grey-text);margin-top:10px;padding:0 20px}
.offer-frame{left:459px;top:1148px;width:275px;height:177px;border:2px solid var(--red)}

/* who */
.who-bg{left:0;top:1691px;width:1200px;height:611px;background:var(--light)}
.who p{font-size:12.5px;line-height:24px;color:var(--grey-text);text-align:justify}
.exp{left:111px;top:2052px;width:142px;height:178px;background:var(--red);color:var(--white);font-family:"Oswald",sans-serif;font-weight:600;padding:22px 0 0 19px}
.exp .rule{position:absolute;left:118px;top:24px;width:3px;height:100px;background:var(--white)}

/* features */
.features{left:0;top:2302px;width:1200px;height:435px;background:linear-gradient(125deg,#a70d0d 0%,#c4151a 45%,#b00f12 100%)}
.feat{top:2477px;width:290px;height:164px;background:rgba(255,255,255,.12);padding:22px 27px}
.feat h4{display:flex;align-items:center;gap:10px;font-family:"Oswald",sans-serif;font-weight:500;font-size:19px;color:var(--white);text-transform:uppercase}
.feat p{margin-top:12px;font-size:11.5px;line-height:24px;color:var(--white)}

/* testimonials */
.quote{top:2900px;width:282px;height:235px;border:1px solid #e2e2e2;background:var(--white)}
.avatar{position:absolute;left:21px;top:17px;width:80px;height:80px;border-radius:50%;border:3px solid var(--red);background:linear-gradient(160deg,#e9e4df,#b9aea4)}
.qmark{position:absolute;left:64px;top:70px;font-family:Georgia,serif;font-weight:700;font-size:44px;line-height:40px;color:var(--red)}
.quote h5{position:absolute;left:112px;top:42px;font-family:"Oswald",sans-serif;font-weight:500;font-size:19px}
.quote .co{position:absolute;left:112px;top:72px;font-size:12px;color:var(--grey-text)}
.quote p{position:absolute;left:27px;top:131px;width:235px;font-size:12.5px;line-height:24px;color:var(--grey-text)}
.slide-arrow{top:3000px;width:34px;height:34px;border-radius:50%;background:#e5e5e5;color:#555;text-align:center;line-height:32px;font-size:18px}

/* footer */
.footer{left:0;top:3232px;width:1200px;height:384px;background:repeating-linear-gradient(45deg,#1e1e1e 0 3px,#181818 3px 6px)}
.foot-brand{left:143px;top:3318px;font-family:"Oswald",sans-serif;font-weight:700;font-size:56px;line-height:80px;color:#9a9a9a;letter-spacing:-1px;text-transform:uppercase}
.foot-col h6{font-family:"Roboto",sans-serif;font-weight:500;font-size:15px;color:var(--white)}
.foot-col ul{list-style:none;margin-top:16px}
.foot-col li{font-size:12.5px;line-height:25.5px;color:#ddd}
.contact-item{left:872px;display:flex;gap:8px;color:#ddd;font-size:12.5px;line-height:18px}
.contact-item b{display:block;font-size:11px;font-weight:700;color:var(--white)}
.foot-rule{left:143px;top:3542px;width:912px;height:1px;background:#444}
.copy{left:0;top:3562px;width:1200px;text-align:center;color:var(--white);font-size:13px}
.chat{left:1089px;top:3507px;width:34px;height:34px;border-radius:50%;background:var(--white);display:flex;align-items:center;justify-content:center}
</style>
</head>
<body>

<header class="abs site-header">
  <div class="abs brand">Brightgate</div>
  <nav class="nav">
    <a class="active" style="left:410px">HOME</a>
    <a style="left:486px">LOCATIONS</a>
    <a style="left:585px">SERVICES</a>
    <a style="left:674px">COUPONS</a>
    <a style="left:762px">REWARDS</a>
  </nav>
  <svg class="abs" style="left:870px;top:33px" width="15" height="15" viewBox="0 0 15 15"><circle cx="6" cy="6" r="4.5" fill="none" stroke="#fff" stroke-width="2"/><line x1="9.5" y1="9.5" x2="13.5" y2="13.5" stroke="#fff" stroke-width="2"/></svg>
  <div class="abs book-btn">BOOK NOW</div>
</header>

<section>
  <div class="abs hero" role="img" aria-label="Red sports car on a road at dusk"></div>
  <div class="abs hero-panel" role="img" aria-label="Front of a red car with a bright headlight"></div>
  <h1 class="abs head hero-title">Brightgate<br><span>Automotive</span><br>Service</h1>
  <div class="abs btn-red" style="left:145px;top:370px;width:115px;height:34px;line-height:34px">GET STARTED</div>
  <div class="abs hero-arrow" style="left:145px;top:540px">&#8249;</div>
  <div class="abs hero-arrow" style="left:185px;top:540px">&#8250;</div>
</section>

<section>
  <div class="abs svc" style="left:0;width:320px;background:var(--red)">
    <h3>Maintenance<br>Services</h3>
    <p>Lorem ipsum dolor sit amet, conse ctetur adipiscing elit, sed do eiusmod tempor incididunt ut labore</p>
    <div class="outline-btn">START NOW</div>
    <div class="num">01</div>
  </div>
  <div class="abs" style="left:320px;top:640px;width:280px;height:267px;background:linear-gradient(150deg,#9a9a9a,#3d3d3d 60%,#1f1f1f)" role="img" aria-label="Mechanic lying under a raised car"></div>
  <div class="abs svc" style="left:600px;width:319px;background:var(--black)">
    <h3>Certified Repair<br>Services</h3>
    <p>Lorem ipsum dolor sit amet, conse ctetur adipiscing elit, sed do eiusmod tempor incididunt ut labore</p>
    <div class="outline-btn">START NOW</div>
    <div class="num">02</div>
  </div>
  <div class="abs" style="left:919px;top:640px;width:281px;height:267px;background:linear-gradient(150deg,#dfe3e8,#7f8a96 55%,#2c3440)" role="img" aria-label="Gloved hands working on an engine with a wrench"></div>
</section>

<section>
  <h2 class="abs head sec-title" style="top:1008px">What <span>We</span> Offer</h2>
  <div class="abs offer-frame"></div>

  <div class="abs offer" style="left:158px;top:1102px">
    <div class="ico"><svg width="44" height="44" viewBox="0 0 44 44" fill="none" stroke="#c0191d" stroke-width="2"><path d="M6 26l4-9h18l4 9v8H6z"/><circle cx="12" cy="30" r="2"/><circle cx="26" cy="30" r="2"/><path d="M30 14l7 3v6c0 5-3 8-7 9-4-1-7-4-7-9v-6z"/><path d="M27 22l2 2 4-4"/></svg></div>
    <h4>DUIS AUTE IRURE</h4>
    <p>Lorem ipsum dolor sit amet, consectetur adipiscing elit, sed do eiusmod tempor incididunt ut labore et dolore</p>
  </div>
  <div class="abs offer active" style="left:459px;top:1102px">
    <div class="ico"><svg width="44" height="44" viewBox="0 0 44 44" fill="none" stroke="#fff" stroke-width="2"><rect x="8" y="14" width="28" height="20" rx="2"/><path d="M13 14v-3h5v3M26 14v-3h5v3"/><path d="M23 18l-4 6h5l-3 6"/></svg></div>
    <h4>DUIS AUTE IRURE</h4>
    <p>Lorem ipsum dolor sit amet, consectetur adipiscing elit, sed do eiusmod tempor incididunt ut labore et dolore</p>
  </div>
  <div class="abs offer" style="left:767px;top:1102px">
    <div class="ico"><svg width="44" height="44" viewBox="0 0 44 44" fill="none" stroke="#c0191d" stroke-width="2"><circle cx="22" cy="22" r="13" stroke-dasharray="4 3"/><circle cx="22" cy="22" r="8"/><path d="M17 17l10 10M27 17l-10 10"/></svg></div>
    <h4>DUIS AUTE IRURE</h4>
    <p>Lorem ipsum dolor sit amet, consectetur adipiscing elit, sed do eiusmod tempor incididunt ut labore et dolore</p>
  </div>

  <div class="abs offer" style="left:158px;top:1383px">
    <div class="ico"><svg width="44" height="44" viewBox="0 0 44 44" fill="none" stroke="#c0191d" stroke-width="2"><path d="M7 30a15 15 0 0 1 30 0z"/><path d="M22 30l5-9"/><path d="M12 24h2M30 24h2M22 18v2"/></svg></div>
    <h4>DUIS AUTE IRURE</h4>
    <p>Lorem ipsum dolor sit amet, consectetur adipiscing elit, sed do eiusmod tempor incididunt ut labore et dolore</p>
  </div>
  <div class="abs offer" style="left:459px;top:1383px">
    <div class="ico"><svg width="44" height="44" viewBox="0 0 44 44" fill="none" stroke="#c0191d" stroke-width="2"><circle cx="18" cy="24" r="9" stroke-dasharray="4 2"/><circle cx="18" cy="24" r="4"/><circle cx="30" cy="14" r="6" stroke-dasharray="3 2"/><circle cx="30" cy="14" r="2"/></svg></div>
    <h4>DUIS AUTE IRURE</h4>
    <p>Lorem ipsum dolor sit amet, consectetur adipiscing elit, sed do eiusmod tempor incididunt ut labore et dolore</p>
  </div>
  <div class="abs offer" style="left:767px;top:1383px">
    <div class="ico"><svg width="44" height="44" viewBox="0 0 44 44" fill="none" stroke="#c0191d" stroke-width="2"><circle cx="22" cy="19" r="11"/><circle cx="22" cy="19" r="5"/><path d="M22 8v6M22 24v6M11 19h6M27 19h6"/><rect x="10" y="32" width="24" height="5" rx="1"/></svg></div>
    <h4>DUIS AUTE IRURE</h4>
    <p>Lorem ipsum dolor sit amet, consectetur adipiscing elit, sed do eiusmod tempor incididunt ut labore et dolore</p>
  </div>
</section>

<section class="who">
  <div class="abs who-bg"></div>
  <div class="abs" style="left:300px;top:1770px;width:323px;height:331px;background:var(--black)"></div>
  <div class="abs" style="left:152px;top:1787px;width:454px;height:415px;background:linear-gradient(140deg,#d7dbe0,#6e737a 50%,#2f3338)" role="img" aria-label="Mechanic kneeling beside a car wheel in a workshop"></div>
  <div class="abs exp">
    <div style="font-size:15px">MORE THAN</div>
    <div style="font-size:48px;line-height:58px">20</div>
    <div style="font-size:15px;line-height:32px">YEARS OF<br>EXPERIENCE</div>
    <div class="rule"></div>
  </div>
  <h2 class="abs head" style="left:640px;top:1798px;font-size:42px;color:var(--grey-head)">Who <span style="color:var(--red)">We</span> Are</h2>
  <p class="abs" style="left:640px;top:1865px;width:413px">Lorem ipsum dolor sit amet, consectetur adipiscing elit, sed do eiusmod tempor incididunt ut labore et dolore magna aliqua. Ut enim ad minim veniam, quis nostrud exercitation ullamco laboris nisi ut aliquip ex ea commodo consequat. Duis aute irure dolor in reprehenderit in voluptate velit esse cillum dolore eu fugiat nulla pariatur.</p>
  <p class="abs" style="left:640px;top:2009px;width:413px">Excepteur sint occaecat cupidatat non proident, sunt in culpa qui officia deserunt mollit anim id est laborum. Lorem ipsum dolor sit amet, consectetur adipiscing elit, sed do eiusmod tempor incididunt ut labore et dolore magna aliqua. Ut enim ad minim veniam, quis nostrud exercitation ullamco laboris nisi ut aliquip ex ea commodo consequat.</p>
  <div class="abs" style="left:640px;top:2147px;width:108px;height:35px;border:2px solid var(--red);color:var(--red);font-family:'Oswald',sans-serif;font-weight:600;font-size:13px;line-height:31px;text-align:center">READ MORE</div>
</section>

<section>
  <div class="abs features"></div>
  <h2 class="abs head" style="left:0;top:2390px;width:1200px;text-align:center;font-size:42px;color:var(--white)">Explore Features</h2>
  <div class="abs feat" style="left:143px">
    <h4><svg width="34" height="34" viewBox="0 0 34 34" fill="none" stroke="#fff" stroke-width="1.8"><path d="M5 29l14-14M22 4a6 6 0 0 0-5 8l2 2a6 6 0 0 0 8-5l-3 1-2-2z"/><path d="M5 5l8 8M5 5l3-1 1 3M20 20l8 8"/></svg>Get A Quote</h4>
    <p>Lorem ipsum dolor sit amet, consectetur adip iscing elit, sed do eiusmod tempor incididunt ut labore et dolore magna aliqua.</p>
  </div>
  <div class="abs feat" style="left:455px">
    <h4><svg width="34" height="34" viewBox="0 0 34 34" fill="none" stroke="#fff" stroke-width="1.8"><rect x="5" y="5" width="20" height="25" rx="2"/><path d="M9 12h12M9 17h12M9 22h6"/><circle cx="25" cy="25" r="6"/><path d="M22 25l2 2 4-4"/></svg>Book Appointment</h4>
    <p>Lorem ipsum dolor sit amet, consectetur adip iscing elit, sed do eiusmod tempor incididunt ut labore et dolore magna aliqua.</p>
  </div>
  <div class="abs feat" style="left:766px">
    <h4><svg width="40" height="34" viewBox="0 0 40 34" fill="none" stroke="#fff" stroke-width="1.8"><path d="M4 20l5-10h22l5 10v8H4z"/><path d="M4 20h32"/><circle cx="11" cy="24" r="2"/><circle cx="29" cy="24" r="2"/><path d="M7 28v3M33 28v3"/></svg>Get Your Car Fixed</h4>
    <p>Lorem ipsum dolor sit amet, consectetur adip iscing elit, sed do eiusmod tempor incididunt ut labore et dolore magna aliqua.</p>
  </div>
</section>

<section>
  <h2 class="abs head sec-title" style="top:2812px">What <span>People</span> Say</h2>
  <div class="abs slide-arrow" style="left:74px">&#8249;</div>
  <div class="abs slide-arrow" style="left:1092px">&#8250;</div>

  <div class="abs quote" style="left:145px">
    <div class="avatar" role="img" aria-label="Customer portrait"></div><div class="qmark">&#8220;</div>
    <h5>John Doe</h5><div class="co">Company name</div>
    <p>Lorem ipsum dolor sit amet, consectetur adipiscing elit, sed do eiusmod tempor incididunt ut labore et dolore</p>
  </div>
  <div class="abs quote" style="left:460px">
    <div class="avatar" role="img" aria-label="Customer portrait"></div><div class="qmark">&#8220;</div>
    <h5>John Doe</h5><div class="co">Company name</div>
    <p>Lorem ipsum dolor sit amet, consectetur adipiscing elit, sed do eiusmod tempor incididunt ut labore et dolore</p>
  </div>
  <div class="abs quote" style="left:776px">
    <div class="avatar" role="img" aria-label="Customer portrait"></div><div class="qmark">&#8220;</div>
    <h5>John Doe</h5><div class="co">Company name</div>
    <p>Lorem ipsum dolor sit amet, consectetur adipiscing elit, sed do eiusmod tempor incididunt ut labore et dolore</p>
  </div>
</section>

<footer>
  <div class="abs footer"></div>
  <div class="abs foot-brand">Brightgate</div>
  <div class="abs foot-col" style="left:453px;top:3322px">
    <h6>Quick Links</h6>
    <ul><li>Home</li><li>About</li><li>Services</li><li>Projects</li><li>Blog</li><li>Contact</li></ul>
  </div>
  <div class="abs foot-col" style="left:643px;top:3322px">
    <h6>About Company</h6>
    <ul><li>Privacy Policy</li><li>Terms of Service</li><li>Site Map</li><li>Imprint</li><li>Terms And Conditions</li></ul>
  </div>
  <div class="abs foot-col" style="left:874px;top:3322px"><h6>Contact Us</h6></div>
  <div class="abs contact-item" style="top:3362px">
    <svg width="14" height="14" viewBox="0 0 14 14"><path d="M3 1l2 3-1 2c1 2 2 3 4 4l2-1 3 2-1 2C6 13 1 8 1 3z" fill="#e0252a"/></svg>
    <div><b>Phone</b>+1 555 014 2288</div>
  </div>
  <div class="abs contact-item" style="top:3410px">
    <svg width="14" height="14" viewBox="0 0 14 14"><rect x="1" y="3" width="12" height="9" fill="#e0252a"/><path d="M1 3l6 5 6-5" stroke="#1b1b1b" fill="none"/></svg>
    <div><b>Email</b>info@brightgate.example</div>
  </div>
  <div class="abs contact-item" style="top:3458px">
    <svg width="14" height="14" viewBox="0 0 14 14"><path d="M7 1a4.5 4.5 0 0 1 4.5 4.5C11.5 9 7 13 7 13S2.5 9 2.5 5.5A4.5 4.5 0 0 1 7 1z" fill="#e0252a"/><circle cx="7" cy="5.5" r="1.6" fill="#1b1b1b"/></svg>
    <div><b>Location</b>123,Lorem ipsum dolor sit<br>amet, consectetur</div>
  </div>
  <div class="abs foot-rule"></div>
  <div class="abs copy">2025 Copyrights - &nbsp;Brightgate &nbsp;| All Rights Reserved</div>
  <div class="abs chat"><svg width="18" height="18" viewBox="0 0 18 18"><path d="M9 2c4 0 7 2.6 7 6s-3 6-7 6l-4 2 1-3C3.5 12 2 10 2 8c0-3.4 3-6 7-6z" fill="#111"/><circle cx="6" cy="8" r="1" fill="#fff"/><circle cx="9" cy="8" r="1" fill="#fff"/><circle cx="12" cy="8" r="1" fill="#fff"/></svg></div>
</footer>

</body>
</html>
```